Business Cards, Letterheads, Envelopes

A company's new identity to be reflected on its stationery items

Target Market(s)

Large Corporate Companies & Enterprises

Font styles to use
Sans Serif

Colors
0555a3
3176b5
85abd2
85cae6
33a6d7
0293ce

```html
<!DOCTYPE html>
<html lang="en">
<head>
<meta charset="utf-8">
<title>Corvanta Systems — Stationery</title>
<link href="https://fonts.googleapis.com/css2?family=Lato:wght@400;700&family=Roboto:wght@400;500&display=swap" rel="stylesheet">
<style>
:root{
  --navy:#0555a3;
  --blue:#3176b5;
  --sky:#33a6d7;
  --brand:#3a8bcf;
  --pale:#85abd2;
  --ink:#3a3a3a;
  --muted:#6b6b6b;
  --paper:#ffffff;
  --backdrop:#dcdcdc;
}
*{margin:0;padding:0;box-sizing:border-box}
html,body{width:1200px;height:851px;overflow:hidden;background:var(--backdrop)}
body{position:relative;font-family:"Lato",sans-serif;color:var(--ink)}
.sheet{position:absolute;background:var(--paper);overflow:hidden}
.brand{display:flex;align-items:center;gap:5px;font-family:"Lato",sans-serif;font-weight:700;color:var(--brand);letter-spacing:.06em;text-transform:uppercase;line-height:1.15}
.brand-dot{border-radius:50%;background:currentColor;flex:none}

/* letterhead */
.letterhead{left:165px;top:139px;width:318px;height:448px}
.letterhead .brand{position:absolute;left:112px;top:20px;font-size:6px}
.letterhead .brand-dot{width:22px;height:22px}
.letter-body{position:absolute;left:51px;top:114px;width:234px;font-size:4.9px;line-height:8.5px;color:var(--muted);text-align:justify}
.letter-body p{margin-bottom:8.5px}
.letter-body .salute{margin-bottom:8.5px}
.letter-body .signoff{margin-top:25px}
.contact{position:absolute;display:flex;font-family:"Roboto",sans-serif;color:var(--ink)}
.contact .addr{padding-right:6px;border-right:.6px solid var(--brand)}
.contact .lines{padding-left:6px;align-self:flex-end}
.letterhead .contact{left:24px;top:400px;font-size:5px;line-height:6.5px}
.web-band{position:absolute;left:0;background:var(--brand);color:#fff;font-family:"Roboto",sans-serif;display:flex;align-items:center}
.letterhead .web-band{top:427px;width:267px;height:11px;padding-left:24px;font-size:5px}
.band-dot{position:absolute;border-radius:50%;border:1px solid var(--brand)}
.letterhead .band-dot{left:271px;top:424px;width:17px;height:17px}

/* folder */
.folder{left:501px;top:139px;width:318px;height:448px;background:linear-gradient(135deg,#3f86c0,var(--blue) 55%,#2a6ca8)}
.folder .brand{position:absolute;left:100px;top:42px;color:#fff;font-size:7px}
.folder .brand-dot{width:30px;height:30px}
.folder-art{position:absolute;left:0;top:170px;width:318px;height:278px;background:linear-gradient(170deg,#3a82bf 0%,#5c9bcf 35%,#dfeaf5 70%,#ffffff 100%)}

/* envelope front */
.envelope{left:165px;top:606px;width:320px;height:139px}
.envelope .brand{position:absolute;left:22px;top:17px;font-size:5.2px}
.envelope .brand-dot{width:19px;height:19px}
.envelope .contact{left:22px;top:97px;font-size:4.4px;line-height:5.2px}
.envelope .web-band{top:119px;width:274px;height:9px;padding-left:22px;font-size:4.4px}
.envelope .band-dot{left:275px;top:116px;width:15px;height:15px}

/* envelope back */
.envelope-back{left:501px;top:607px;width:318px;height:140px;background:transparent}
.envelope-back .pocket{position:absolute;inset:0;background:var(--paper)}
.envelope-back .flap{position:absolute;left:0;top:0}
.envelope-back .flap-dot{position:absolute;left:149px;top:11px;width:20px;height:20px;border-radius:50%;border:1.2px solid #fff}

/* business cards */
.card{position:absolute;width:133px;height:78px;overflow:hidden}
.card-front{left:856px;top:234px;background:var(--brand)}
.card-art{position:absolute;left:0;top:0;width:56px;height:78px;background:linear-gradient(160deg,#6fb0e3,#2f7fc3)}
.card-front .brand{position:absolute;left:66px;top:52px;color:#fff;font-size:5px}
.card-front .brand-dot{width:6px;height:6px}
.card-back{left:856px;top:331px;background:var(--paper)}
.card-band{position:absolute;left:0;top:12px;width:133px;height:12px;background:var(--brand)}
.card-person{position:absolute;left:11px;top:14px;color:#fff;font-family:"Roboto",sans-serif;line-height:4.2px}
.card-person .name{font-size:4px;font-weight:500}
.card-person .role{font-size:2.8px}
.card-back .brand{position:absolute;left:73px;top:15px;font-size:3.2px;background:#fff;padding:1px 3px;border-radius:1px}
.card-back .brand-dot{width:5px;height:5px}
.card-info{position:absolute;left:11px;top:36px;font-family:"Roboto",sans-serif;font-size:2.8px;line-height:3.8px;color:var(--ink)}
.card-rule{width:6px;height:.6px;background:var(--brand);margin:3px 0 2px}
.card-info .row{display:flex;align-items:center;gap:2px}
.card-info svg{width:3px;height:3px;fill:var(--brand)}
</style>
</head>
<body>

<section class="sheet letterhead">
  <div class="brand"><span class="brand-dot"></span><span>Corvanta Systems<br>Private Limited</span></div>
  <div class="letter-body">
    <p class="salute">Dear Daniel Harrow,</p>
    <p>Lorem ipsum dolor sit amet, consectetuer adipiscing elit, sed diam nonummy nibh euismod tincidunt ut laoreet dolore magna aliquam erat volutpat. Ut wisi enim ad minim veniam, quis nostrud exerci tation ullamcorper suscipit lobortis nisl ut aliquip ex ea commodo consequat. Duis dolore te feugait nulla facilisi. Nam liber tempor cum soluta nobis eleifend option congue nihil imperdiet doming id quod mazim placerat facer possim assum. Lorem ipsum dolor sit amet, consectetuer adipiscing elit, sed diam nonummy nibh euismod tincidunt ut laoreet dolore magna aliquam erat volutpat. Ut wisi enim ad minim veniam, quis nostrud exerci tation ullamcorper suscipit lobortis nisl ut aliquip ex ea commodo consequat.</p>
    <p>Consectetuer adipiscing elit, sed diam nonummy nibh euismod tincidunt ut laoreet dolore magna aliquam erat volutpat. Ut wisi enim ad minim veniam, quis nostrud exerci tation ullamcorper suscipit lobortis nisl ut aliquip ex ea commodo consequat. Consectetuer adipiscing elit, sed diam nonummy nibh euismod tincidunt ut laoreet dolore magna aliquam erat volutpat. Ut wisi enim ad minim veniam, quis nostrud exerci tation ullamcorper suscipit lobortis nisl ut aliquip ex ea commodo consequat.</p>
    <p>Consectetuer adipiscing elit, sed diam nonummy nibh euismod tincidunt ut laoreet dolore magna aliquam erat volutpat. Ut wisi enim ad minim veniam, quis nostrud exerci tation ullamcorper suscipit lobortis nisl ut aliquip ex ea commodo consequat. Consectetuer adipiscing elit, sed diam nonummy nibh euismod tincidunt ut laoreet dolore magna aliquam erat volutpat. Ut wisi enim ad minim veniam, quis nostrud exerci tation ullamcorper suscipit lobortis nisl ut aliquip ex ea commodo consequat.</p>
    <p class="signoff">Sincerely Yours</p>
  </div>
  <div class="contact">
    <div class="addr">Corvanta Systems (Pvt) Ltd.<br>114B, Lakeview Tech Park<br>Vijaynagar, Mysore, Karnataka</div>
    <div class="lines">P. +91 821 555 0192<br>E. info@corvantasys.com</div>
  </div>
  <div class="web-band">www.corvantasys.com</div>
  <span class="band-dot"></span>
</section>

<section class="sheet folder">
  <div class="brand"><span class="brand-dot"></span><span>Corvanta Systems<br>Private Limited</span></div>
  <div class="folder-art" role="img" aria-label="Large network graphic of connected nodes and lines in brand blue"></div>
</section>

<section class="sheet envelope">
  <div class="brand"><span class="brand-dot"></span><span>Corvanta Systems<br>Private Limited</span></div>
  <div class="contact">
    <div class="addr">Corvanta Systems (Pvt) Ltd.<br>114B, Lakeview Tech Park<br>Vijaynagar, Mysore, Karnataka</div>
    <div class="lines">P. +91 821 555 0192<br>E. info@corvantasys.com</div>
  </div>
  <div class="web-band">www.corvantasys.com</div>
  <span class="band-dot"></span>
</section>

<section class="sheet envelope-back">
  <div class="pocket"></div>
  <svg class="flap" width="318" height="46" viewBox="0 0 318 46">
    <path d="M0 0H318L307 40Q305 45 299 45H19Q13 45 11 40Z" fill="var(--brand)"/>
  </svg>
  <span class="flap-dot"></span>
</section>

<section class="card card-front">
  <div class="card-art" role="img" aria-label="White network graphic of connected nodes"></div>
  <div class="brand"><span class="brand-dot"></span><span>Corvanta Systems<br>Private Limited</span></div>
</section>

<section class="card card-back">
  <div class="card-band"></div>
  <div class="card-person"><div class="name">Arjun Mehta</div><div class="role">CEO &amp; Founder</div></div>
  <div class="brand"><span class="brand-dot"></span><span>Corvanta Systems<br>Private Limited</span></div>
  <div class="card-info">
    Corvanta Systems (Pvt) Ltd.<br>114B, Lakeview Tech Park<br>Vijaynagar, Mysore, Karnataka
    <div class="card-rule"></div>
    <div class="row"><svg viewBox="0 0 10 10"><path d="M2 0h2l1 3-1.5 1a6 6 0 0 0 2.5 2.5L7 5l3 1v2c0 1-1 2-2 2C4 10 0 6 0 2c0-1 1-2 2-2z"/></svg>+91 821 555 0192</div>
    <div class="row"><svg viewBox="0 0 10 10"><path d="M0 2h10v6H0z"/></svg>info@corvantasys.com</div>
    <div class="row"><svg viewBox="0 0 10 10"><circle cx="5" cy="5" r="5"/></svg>www.corvantasys.com</div>
  </div>
</section>

</body>
</html>
```